LuMarking-Tagvelory Partial Redesign - Web App

Are you able to apply your creativity to an existing layout? I’m convinced that even just a few touches can make a big difference to add personality and professionalism to a website design, and I’m looking for someone able to use existing ideas and bring them to the next level while keeping inside some given constraints.
The actual job is to improve an existing design concept and to apply it creatively to a landing page, a simple home page, and an older web app (single page website).
To help you start with a clear picture of the current situation and of my requirements, I created a detailed brief with screenshots, live examples, and complete instructions. You can find it attached to this job.
My tastes are inclined towards clean and simple designs. For this project I'm not looking for dazzling novelty, but for very solid craftsmanship. Are the right man - or woman - for the job?
Updates
I wanted to thank everybody who participated in this project. I made a choice, but also other designs were interesting. Hope to work with you another time.
Target Market(s)
Our main target is social media marketers and startuppers
Look and feel
Each slider illustrates characteristics of the customer's brand and the style your logo design should communicate.

```html
<!DOCTYPE html>
<html lang="en">
<head>
<meta charset="utf-8">
<title>LuMarking – Hashtag Summary</title>
<link rel="stylesheet" href="https://fonts.googleapis.com/css2?family=Open+Sans:wght@400;600;700&display=swap">
<style>
:root{
  --dark:#1f1f1f;
  --blue:#0a6fd1;
  --text:#555;
  --light-band:#ececec;
  --white:#fff;
  --red:#dc3912;
  --orange:#ff9900;
  --green:#109618;
  --pie-blue:#3366cc;
}
*{margin:0;padding:0;box-sizing:border-box}
html,body{width:800px;height:1200px;overflow:hidden}
body{font-family:"Open Sans",Arial,sans-serif;color:var(--text);background:var(--white);position:relative}
.site-header{position:absolute;top:0;left:0;width:800px;height:94px;background:linear-gradient(#262626,#1a1a1a)}
.brand{position:absolute;left:76px;top:30px;display:flex;align-items:center;gap:10px}
.brand-mark{width:22px;height:22px;background:#cfcfcf}
.brand-name{font-size:26px;font-weight:700;color:#cfcfcf;line-height:1}
.brand-tag{position:absolute;left:108px;top:61px;font-size:9px;color:#aaa}
.main-nav{position:absolute;top:44px;left:529px;display:flex;gap:5px}
.nav-btn{height:19px;padding:0 9px;font-size:7px;font-weight:700;color:#fff;background:linear-gradient(#4a4a4a,#2e2e2e);border:1px solid #555;border-radius:2px;display:flex;align-items:center}
.nav-btn.active{background:linear-gradient(#1a7fe0,#0053b0);border-color:#0a5bb5;width:62px;justify-content:center}
.nav-sep{width:1px;height:19px;background:#555;margin:0 2px}
.page-head{position:absolute;top:94px;left:0;width:800px;height:140px;background:linear-gradient(#fff,var(--light-band));border-bottom:1px solid #cfcfcf}
.page-title{position:absolute;left:76px;top:24px;font-size:20px;font-weight:700;color:#666}
.page-title span{color:var(--blue)}
.tracked{position:absolute;left:76px;top:52px;font-size:11px;font-style:italic;color:var(--blue)}
.tracked b{font-weight:700}
.tabs{position:absolute;left:76px;top:93px;display:flex;gap:11px}
.tab{width:75px;height:21px;font-size:9.5px;font-weight:700;color:var(--blue);background:linear-gradient(#fafafa,#dcdcdc);border:1px solid #bbb;display:flex;align-items:center;justify-content:center}
.tab.active{color:#fff;background:linear-gradient(#1a7fe0,#0050aa);border-color:#0a4f9e}
.stats{position:absolute;top:268px;left:82px;display:flex;gap:4px}
.stat{width:124px;height:58px;transform:skewX(-8deg);background:linear-gradient(#f4f4f4,#d6d6d6);border:1px solid #ddd;display:flex;flex-direction:column;align-items:center;justify-content:center}
.stat>*{transform:skewX(8deg)}
.stat-value{font-size:17px;font-weight:700;color:#555}
.stat-label{font-size:8px;font-weight:600;color:#555}
.stat.primary{background:linear-gradient(#2a8ae8,#0058b5);border-color:#0b5cb4}
.stat.primary .stat-value,.stat.primary .stat-label{color:#fff}
.section-rule{position:absolute;left:0;width:800px;height:4px;background:linear-gradient(#d0d0d0,#f6f6f6)}
.section-title{position:absolute;left:0;width:800px;text-align:center;font-size:18px;font-weight:700;color:#444;text-decoration:underline;text-underline-offset:3px}
.chart-label{position:absolute;font-size:11px;font-weight:600;color:#444;letter-spacing:.5px;display:flex;align-items:center;gap:4px}
.person{display:inline-block;width:4px;height:13px;border-radius:2px}
.person.red{background:var(--red)}
.person.blue{background:var(--pie-blue)}
.gauge{position:absolute;width:204px;height:204px}
.pie{position:absolute;width:140px;height:140px}
.legend{position:absolute;font-size:8px;color:#333;line-height:11px}
.legend-item{display:flex;gap:4px}
.legend-swatch{width:9px;height:9px;flex:none;margin-top:1px}
.site-footer{position:absolute;top:1104px;left:0;width:800px;height:96px;background:linear-gradient(#262626,#1a1a1a)}
.footer-brand{position:absolute;left:92px;top:36px;display:flex;align-items:center;gap:7px}
.footer-brand .brand-mark{width:14px;height:14px}
.footer-brand .brand-name{font-size:17px}
.footer-tag{position:absolute;left:113px;top:57px;font-size:6.5px;color:#999}
.footer-copy{position:absolute;left:273px;top:44px;font-size:7.5px;color:#aaa;line-height:12px}
.footer-addr{position:absolute;left:450px;top:46px;font-size:7.5px;color:#aaa;line-height:11px}
.footer-social{position:absolute;left:604px;top:46px;display:flex;gap:3px}
.footer-social span{width:17px;height:17px;border-radius:3px}
</style>
</head>
<body>
<header class="site-header">
  <div class="brand"><div class="brand-mark"></div><div class="brand-name">LuMarking</div></div>
  <div class="brand-tag">Smart Social Tagging Insights</div>
  <nav class="main-nav">
    <div class="nav-btn active">Products ▾</div>
    <div class="nav-sep"></div>
    <div class="nav-btn">Blog</div>
    <div class="nav-btn">About</div>
    <div class="nav-sep"></div>
    <div class="nav-btn">● ▾</div>
  </nav>
</header>

<section class="page-head">
  <h1 class="page-title">Hashtag: <span>#socialtips</span></h1>
  <p class="tracked"><b>Tracked influencers:</b> @danoverhill, @ritamarlowmedia</p>
  <div class="tabs">
    <div class="tab active">Summary</div>
    <div class="tab">Timeline</div>
    <div class="tab">Influencers</div>
    <div class="tab">Hashtags</div>
  </div>
</section>

<div class="stats">
  <div class="stat"><div class="stat-value">8</div><div class="stat-label">Observed Days</div></div>
  <div class="stat primary"><div class="stat-value">8,234,567</div><div class="stat-label">Total Impressions</div></div>
  <div class="stat primary"><div class="stat-value">840</div><div class="stat-label">Total Tweets</div></div>
  <div class="stat"><div class="stat-value">1,076,658</div><div class="stat-label">Daily Impressions</div></div>
  <div class="stat"><div class="stat-value">145</div><div class="stat-label">Daily Tweets</div></div>
</div>

<div class="section-rule" style="top:366px"></div>
<h2 class="section-title" style="top:396px">TREND ANALYSIS</h2>

<div class="chart-label" style="left:121px;top:470px">Trend With Your Influencers <i class="person red"></i><i class="person red"></i><i class="person blue"></i></div>
<div class="chart-label" style="left:470px;top:470px">Trend Without Your Influencers <i class="person red"></i><i class="person red"></i></div>

<svg class="gauge" style="left:121px;top:508px" viewBox="-102 -102 204 204" role="img" aria-label="Trend gauge with influencers, value 3">
  <circle r="100" fill="#c8c8c8"/><circle r="94" fill="#e2e2e2"/><circle r="89" fill="#f7f7f7"/>
  <path d="M-61.5 61.5A87 87 0 0 1-55.9-66.6L-46.3-55.2A72 72 0 0 0-50.9 50.9Z" fill="var(--red)"/>
  <path d="M-55.9-66.6A87 87 0 0 1 55.9-66.6L46.3-55.2A72 72 0 0 0-46.3-55.2Z" fill="var(--orange)"/>
  <path d="M55.9-66.6A87 87 0 0 1 61.5 61.5L50.9 50.9A72 72 0 0 0 46.3-55.2Z" fill="var(--green)"/>
  <path d="M0-72V-88M-77 -30L-64-24M77-30L64-24" stroke="#333" stroke-width="1.5"/>
  <text x="0" y="-28" text-anchor="middle" font-size="21" fill="#333" font-family="Arial,sans-serif">Trend</text>
  <text x="-44" y="47" text-anchor="middle" font-size="12" fill="#333" font-family="Arial,sans-serif">-100</text>
  <text x="44" y="47" text-anchor="middle" font-size="12" fill="#333" font-family="Arial,sans-serif">100</text>
  <text x="0" y="74" text-anchor="middle" font-size="19" fill="#111" font-family="Arial,sans-serif">3</text>
  <path d="M-3 32L6-82L4 32Z" fill="#e8684a" stroke="#c44" stroke-width=".5"/>
  <circle r="13" fill="#4a86e8"/>
</svg>

<svg class="gauge" style="left:471px;top:508px" viewBox="-102 -102 204 204" role="img" aria-label="Trend gauge without influencers, value 3">
  <circle r="100" fill="#c8c8c8"/><circle r="94" fill="#e2e2e2"/><circle r="89" fill="#f7f7f7"/>
  <path d="M-61.5 61.5A87 87 0 0 1-55.9-66.6L-46.3-55.2A72 72 0 0 0-50.9 50.9Z" fill="var(--red)"/>
  <path d="M-55.9-66.6A87 87 0 0 1 55.9-66.6L46.3-55.2A72 72 0 0 0-46.3-55.2Z" fill="var(--orange)"/>
  <path d="M55.9-66.6A87 87 0 0 1 61.5 61.5L50.9 50.9A72 72 0 0 0 46.3-55.2Z" fill="var(--green)"/>
  <path d="M0-72V-88M-77 -30L-64-24M77-30L64-24" stroke="#333" stroke-width="1.5"/>
  <text x="0" y="-28" text-anchor="middle" font-size="21" fill="#333" font-family="Arial,sans-serif">Trend</text>
  <text x="-44" y="47" text-anchor="middle" font-size="12" fill="#333" font-family="Arial,sans-serif">-100</text>
  <text x="44" y="47" text-anchor="middle" font-size="12" fill="#333" font-family="Arial,sans-serif">100</text>
  <text x="0" y="74" text-anchor="middle" font-size="19" fill="#111" font-family="Arial,sans-serif">3</text>
  <path d="M-3 32L6-82L4 32Z" fill="#e8684a" stroke="#c44" stroke-width=".5"/>
  <circle r="13" fill="#4a86e8"/>
</svg>

<div class="section-rule" style="top:761px"></div>
<h2 class="section-title" style="top:788px">YOUR INFLUENCERS ANALYSIS</h2>

<div class="chart-label" style="left:77px;top:862px">Your Influencers <i class="person blue"></i> vs Rest Of The Internet <i class="person red"></i><i class="person red"></i></div>
<div class="chart-label" style="left:445px;top:862px">Your Influencers <i class="person blue"></i> vs Your Influencers <i class="person blue"></i></div>

<svg class="pie" style="left:142px;top:901px" viewBox="-70 -70 140 140" role="img" aria-label="Pie chart: tracked influencers 14.9%, others 85.1%">
  <path d="M0 0L51.5-38A64 64 0 1 1 0-64Z" fill="var(--red)" stroke="#fff" stroke-width="1"/>
  <path d="M0 0L0-64A64 64 0 0 1 51.5-38Z" fill="var(--pie-blue)" stroke="#fff" stroke-width="1"/>
  <text x="20" y="-38" text-anchor="middle" font-size="8" fill="#fff" font-family="Arial,sans-serif">14.9%</text>
  <text x="-22" y="44" text-anchor="middle" font-size="8" fill="#fff" font-family="Arial,sans-serif">85.1%</text>
</svg>
<div class="legend" style="left:289px;top:903px">
  <div class="legend-item"><span class="legend-swatch" style="background:var(--pie-blue)"></span><span>Tracked<br>Influencers</span></div>
  <div class="legend-item"><span class="legend-swatch" style="background:var(--red)"></span><span>Others</span></div>
</div>

<svg class="pie" style="left:490px;top:901px" viewBox="-70 -70 140 140" role="img" aria-label="Pie chart: greyfoxnote 8.1%, jonaskerrow 91.9%">
  <path d="M0 0L31.2-55.9A64 64 0 1 1 0-64Z" fill="var(--red)" stroke="#fff" stroke-width="1"/>
  <path d="M0 0L0-64A64 64 0 0 1 31.2-55.9Z" fill="var(--pie-blue)" stroke="#fff" stroke-width="1"/>
  <text x="11" y="-46" text-anchor="middle" font-size="8" fill="#fff" font-family="Arial,sans-serif">8.1%</text>
  <text x="-13" y="48" text-anchor="middle" font-size="8" fill="#fff" font-family="Arial,sans-serif">91.9%</text>
</svg>
<div class="legend" style="left:638px;top:903px">
  <div class="legend-item"><span class="legend-swatch" style="background:var(--pie-blue)"></span><span>greyfoxnote</span></div>
  <div class="legend-item"><span class="legend-swatch" style="background:var(--red)"></span><span>jonaskerrow</span></div>
</div>

<footer class="site-footer">
  <div class="footer-brand"><div class="brand-mark"></div><div class="brand-name">LuMarking</div></div>
  <div class="footer-tag">Smart Social Tagging Insights</div>
  <div class="footer-copy">Copyright © 2012. All Rights Reserved.<br>Privacy Policy | Terms of Use</div>
  <div class="footer-addr">48 Fenwick Lane<br>N7 4QL Harbury, UK</div>
  <div class="footer-social">
    <span style="background:#4fb3e8"></span>
    <span style="background:#3b5b9a"></span>
    <span style="background:#c4302b"></span>
    <span style="background:#f28a1c"></span>
  </div>
</footer>
</body>
</html>
```